Business Cards and Logo

KWM - Personal Injury Attorneys is the name of the firm.
We are personal injury lawyers. We want a crisp, modern and impactful design.
Color schemes are white, matte black and light grey OR white, matte black and red OR white, matte black and a nice blue or yellow.
For logo - we don’t want typical logos like scales of justice or a hammer. We want a general design with the KWM letters.
Target Market(s)
People who need attorneys.
Industry/Entity Type
Law Firm
Contact Information for Business Card
Back side: text: Los Angeles - Santa Ana - San Diego - San Francisco
Front side
Name of firm and logo.
Marco Feltrovski
812 W. Colter Ave. 4th Floor
Glendale, CA 91207
(818)555-0172 (c)
(818)555-0194 (o)
Marco@fieldcounselwest.example
Logo Text
KWM
Font styles to use
Other font styles liked:
- Musk - regular. Military - regular. Moonglade. Future. Or similar fonts.
Requirements
Must have
- See above. Nothing else to provide.
- KWM - Personal Injury Attorneys is the name of the firm.
- We are personal injury lawyers. We want a crisp, modern and impactful design.
- Color schemes are white, matte black and light grey OR white, matte black and red OR white, matte black and a nice blue or yellow.
- For logo - we don’t want typical logos like scales of justice or a hammer. We want a general design with the KWM letters.
Nice to have
- See above - nothing else to provide.
Should not have

```html
<!DOCTYPE html>
<html lang="en">
<head>
<meta charset="utf-8">
<title>KWM - Personal Injury Attorneys · Business Cards</title>
<link rel="stylesheet" href="https://fonts.googleapis.com/css2?family=Arimo:wght@400;700&display=swap">
<style>
  :root {
    --brand-blue: #2b78bb;
    --brand-blue-deep: #1f63a3;
    --ink: #3a3a3c;
    --paper: #ffffff;
    --stage: #e6e8ec;
    --card-shadow: 0 18px 40px rgba(20, 30, 45, 0.22);
  }
  * { box-sizing: border-box; margin: 0; padding: 0; }
  html, body { width: 1200px; height: 800px; overflow: hidden; }
  body {
    background: var(--stage);
    font-family: "Arimo", Arial, sans-serif;
    position: relative;
  }
  .card {
    position: absolute;
    width: 560px;
    height: 320px;
    border-radius: 22px;
    box-shadow: var(--card-shadow);
    overflow: hidden;
  }

  /* Back side */
  .card-back {
    left: 70px;
    top: 70px;
    background: var(--brand-blue);
    color: var(--paper);
  }
  .card-back .firm-mark {
    position: absolute;
    left: 0; right: 0; top: 78px;
    text-align: center;
  }
  .firm-mark .mark-name {
    display: inline-flex;
    align-items: center;
    gap: 14px;
    font-weight: 700;
    font-size: 64px;
    letter-spacing: 10px;
    line-height: 1;
  }
  .firm-mark .mark-square {
    width: 18px; height: 18px;
    display: inline-block;
  }
  .firm-mark .mark-tagline {
    display: block;
    margin-top: 12px;
    font-weight: 700;
    font-size: 15px;
    letter-spacing: 2.5px;
    text-transform: uppercase;
  }
  .card-back .mark-square { background: var(--paper); }
  .card-back .office-cities {
    position: absolute;
    left: 0; right: 0; bottom: 62px;
    text-align: center;
    font-size: 17px;
    letter-spacing: 1.2px;
  }

  /* Front side */
  .card-front {
    left: 570px;
    top: 410px;
    background: var(--paper);
    color: var(--ink);
  }
  .card-front::after {
    content: "";
    position: absolute;
    left: 0; right: 0; bottom: 0;
    height: 8px;
    background: var(--brand-blue);
  }
  .card-front .firm-mark {
    position: absolute;
    left: 60px; top: 44px;
    color: var(--brand-blue);
    text-align: left;
  }
  .card-front .firm-mark .mark-name { font-size: 50px; letter-spacing: 8px; }
  .card-front .firm-mark .mark-tagline { font-size: 12px; letter-spacing: 2px; margin-top: 8px; }
  .card-front .mark-square { background: var(--brand-blue); width: 15px; height: 15px; }

  .card-front .divider {
    position: absolute;
    height: 1.5px;
    background: var(--brand-blue);
  }
  .divider-main { left: 60px; right: 30px; top: 152px; }
  .divider-contact { left: 40px; width: 220px; top: 218px; }

  .person {
    position: absolute;
    left: 210px; top: 136px;
    background: var(--paper);
    padding: 0 10px;
    text-align: right;
  }
  .person-name { font-weight: 700; font-size: 21px; color: var(--ink); }
  .person-role { font-size: 13px; color: var(--brand-blue); margin-top: 2px; }

  .office-address {
    position: absolute;
    right: 34px; top: 94px;
    text-align: right;
    font-size: 13px;
    line-height: 1.45;
    color: var(--ink);
  }

  .contact-list {
    position: absolute;
    left: 44px; top: 230px;
    list-style: none;
    font-size: 13px;
    line-height: 1.55;
    color: var(--ink);
  }
  .contact-list li { display: flex; align-items: center; gap: 10px; }
  .contact-list svg { width: 13px; height: 13px; flex: none; }
</style>
</head>
<body>

  <section class="card card-back" aria-label="Business card, back side">
    <div class="firm-mark">
      <span class="mark-name"><span class="mark-square"></span>KWM</span>
      <span class="mark-tagline">Personal Injury Attorneys</span>
    </div>
    <p class="office-cities">Los Angeles - Santa Ana - San Diego - San Francisco</p>
  </section>

  <section class="card card-front" aria-label="Business card, front side">
    <div class="firm-mark">
      <span class="mark-name"><span class="mark-square"></span>KWM</span>
      <span class="mark-tagline">Personal Injury Attorneys</span>
    </div>

    <div class="divider divider-main"></div>
    <div class="person">
      <p class="person-name">Marco Feltrovski</p>
      <p class="person-role">Advocate</p>
    </div>

    <address class="office-address" style="font-style: normal;">
      812 W. Colter Ave. 4th Floor<br>
      Glendale, CA 91207
    </address>

    <div class="divider divider-contact"></div>
    <ul class="contact-list">
      <li>
        <svg viewBox="0 0 14 14" aria-hidden="true"><rect x="3" y="1" width="8" height="12" rx="1.5" fill="none" stroke="#2b78bb" stroke-width="1.6"/></svg>
        (818)555-0172
      </li>
      <li>
        <svg viewBox="0 0 14 14" aria-hidden="true"><path d="M3 1.5 L5.5 1.5 L6.5 4.5 L5 5.8 C5.8 7.6 6.8 8.6 8.3 9.3 L9.6 7.8 L12.5 8.8 L12.5 11.3 C12.5 12 12 12.5 11.3 12.5 C6 12.2 1.8 8 1.5 2.7 C1.5 2 2 1.5 3 1.5 Z" fill="#2b78bb"/></svg>
        (818)555-0194
      </li>
      <li>
        <svg viewBox="0 0 14 14" aria-hidden="true"><rect x="1" y="3" width="12" height="8.5" fill="#2b78bb"/><path d="M1.5 3.5 L7 8 L12.5 3.5" fill="none" stroke="#ffffff" stroke-width="1.1"/></svg>
        Marco@fieldcounselwest.example
      </li>
    </ul>
  </section>

</body>
</html>
```